現在ホームページリニューアルを検討しております。
社内でのデザインだとどうしても前情報がある分、発想の限界、偏りがどうしてもあります。

今回はなるべくフラットな状態でデザインを検討したいと考えておりますので、こちらで公募をさせていただくことにしました。

既存の歯科医院のデザインやイメージに縛られることなく、自由な発想でご提案頂きたいと思っております。

■依頼内容

PC・スマートフォン用 それぞれ1枚 合計2枚
(実装する際にはレスポンシブの予定です。)

診療科目は
小児
一般
矯正(大学から月に数回先生にお越し頂いています)

医院の特徴
ショッピングモール内にあります
駐車場あり
バリアフリー
お子さんの遊びスペースあり
デザイナー物件

ページ数
2ページ
希望イメージ
シンプル 複雑
単色 カラフル
暗い 明るい
日常 高級
遊び心 厳粛
未来的 伝統的
女性的 男性的
納品ファイル
• 高解像度JPG (.jpg)
• フォトショップ形式 (.psd)
• PNG形式 (.png)
▼弊社が用意するもの
・ページ構成
・テキスト
・ワイヤーフレーム
・ロゴ
・写真
※受注者様のご意向があれば、ビデオ通話などで対応することも可能です。
※ページ構成や画像などは、個別に送らせていただきたいので、まずはご提案またはメッセージにてご連絡ください。

▼依頼の流れ
1.ご提案
ご提案をいただき次第、弊社よりTOPページの構成をお送りします。
3.デザイン作成
デザインを作成しましたら、提案の【追記する】からデザインファイルの追加をしてください。
5.修正依頼
修正していただきたい箇所がある場合は、修正依頼をいたしますので、修正案を再提案してください。
6.納品
フォトショップ(psd)またはイラストレーター(ai)形式で納品をしていただきます。納品が完了次第、当選を行います。

弊社では、複数のWEBサイトを運用しております。
今回はTOPページのみの依頼となっておりますが、継続的に依頼をさせていただくことも考えております。
ご提案をお待ちしております。
ワイヤーフレームと写真素材を添付します。
依頼金額を45000円に変更して、延長しました。
たくさんのご応募ありがとうございます。
現在、選考中です。3~7日程度で当選デザインを決定できるかと思いますので、今しばらくお待ちください。

歯科医院スタッフの投票にて決定いたしました。

たくさんのご提案ありがとうございます。また機会があれば、是非よろしくお願いいたします。

```html
<!DOCTYPE html>
<html lang="ja">
<head>
<meta charset="utf-8">
<title>あおば歯科医院</title>
<link rel="stylesheet" href="https://fonts.googleapis.com/css2?family=Noto+Sans+JP:wght@400;500;700&family=Noto+Serif+JP:wght@500;700&display=swap">
<style>
:root{
  --blue:#2b7fd6;
  --blue-deep:#1c5fae;
  --navy:#22324a;
  --text:#3d4654;
  --muted:#8a93a0;
  --line:#dfe4ea;
  --pale:#f3f6f9;
  --white:#fff;
}
*{box-sizing:border-box;margin:0;padding:0}
html,body{width:1200px;height:4044px;overflow:hidden}
body{font-family:"Noto Sans JP",sans-serif;color:var(--text);background:var(--white);position:relative;font-size:14px}
.serif{font-family:"Noto Serif JP",serif}
.abs{position:absolute}

/* header */
.hero{left:0;top:0;width:1200px;height:620px;background:linear-gradient(100deg,#eef0f2 0%,#f7f7f6 45%,#e6e9ec 100%)}
.topline{left:12px;top:6px;font-size:11px;color:var(--muted)}
.logo{left:0;width:1200px;top:28px;text-align:center;font-family:"Noto Serif JP",serif;font-size:30px;font-weight:700;color:var(--navy);letter-spacing:.12em}
.contact{left:870px;top:20px;display:flex;gap:12px;align-items:center}
.contact .hours{font-size:10px;color:var(--muted);line-height:1.5}
.contact .tel{font-size:22px;font-weight:700;color:var(--navy)}
.btn-web{background:var(--blue);color:#fff;font-size:13px;padding:10px 14px;border-radius:2px}
.nav{left:290px;top:108px;width:620px;height:50px;display:flex;background:rgba(255,255,255,.85)}
.nav div{flex:1;text-align:center;font-size:14px;color:var(--navy);padding-top:7px;border-left:1px solid var(--line)}
.nav div:first-child{border-left:none}
.nav small{display:block;font-size:9px;color:var(--blue);letter-spacing:.06em}
.hero-copy{left:40px;top:280px;width:360px}
.hero-copy h1{font-family:"Noto Serif JP",serif;font-size:38px;color:var(--navy);letter-spacing:.08em;padding-bottom:12px;border-bottom:1px solid #9aa6b4;margin-bottom:18px}
.hero-copy p{font-size:13px;line-height:2;color:var(--text)}
.hero-btn{left:780px;top:560px;width:290px;height:48px;background:var(--blue);color:#fff;font-size:16px;display:flex;align-items:center;justify-content:center;gap:14px}

/* concerns */
.sec-title{left:0;width:1200px;text-align:center;font-family:"Noto Serif JP",serif;font-size:30px;color:var(--navy);letter-spacing:.06em}
.sec-lead{left:0;width:1200px;text-align:center;font-size:13px;line-height:2;color:var(--text)}
.side-photo{left:760px;top:800px;width:440px;height:620px;background:linear-gradient(160deg,#e9edf0,#cfd6dc 60%,#e8ecef)}
.cards{left:220px;top:840px;width:560px;display:grid;grid-template-columns:repeat(3,176px);gap:16px 16px}
.card{height:188px;background:#fff;border:1px solid var(--line);box-shadow:0 2px 6px rgba(0,0,0,.05);text-align:center;padding-top:16px}
.card h3{font-size:14px;color:var(--navy);font-weight:500;margin-bottom:8px}
.card .icon{width:56px;height:56px;margin:0 auto 10px;background:linear-gradient(#e4eef9,#cfe0f3);border-radius:6px}
.card p{font-size:10px;line-height:1.6;color:var(--muted);padding:0 12px}

/* concept */
.concept{left:0;top:1540px;width:1200px;height:540px;background:linear-gradient(120deg,var(--blue-deep),var(--blue) 55%,#5aa3e6)}
.concept .sec-title{color:#fff;top:70px}
.concept .sec-title::after{content:"";display:block;width:40px;height:1px;background:#fff;margin:12px auto 0}
.concept .en{top:120px;left:0;width:1200px;text-align:center;font-size:11px;color:#dbe9f8}
.circles{left:240px;top:170px;width:720px;display:flex;justify-content:space-between}
.circle-item{width:200px;text-align:center;color:#fff}
.circle{width:170px;height:170px;border-radius:50%;background:#fff;margin:0 auto 22px;color:var(--blue);display:flex;flex-direction:column;align-items:center;justify-content:center;box-shadow:0 0 0 6px rgba(255,255,255,.25)}
.circle .num{font-family:"Noto Serif JP",serif;font-size:28px;line-height:1}
.circle .lbl{font-size:10px;margin-bottom:6px}
.circle b{font-family:"Noto Serif JP",serif;font-size:16px;color:var(--navy);line-height:1.4}
.circle-item p{font-size:12px;line-height:1.8}

/* news */
.news-photo{left:0;top:2380px;width:240px;height:380px;background:linear-gradient(180deg,#eef1f3,#dfe5e2 60%,#cfd9d2)}
.news-list{left:240px;top:2380px;width:720px;background:#fff;border:1px solid var(--line)}
.news-list li{list-style:none;display:flex;gap:24px;height:38px;align-items:center;padding:0 24px;border-bottom:1px solid var(--line);font-size:13px}
.news-list li:last-child{border-bottom:none}
.news-list .date{color:var(--blue);width:90px}

/* greeting */
.greet{left:0;top:2860px;width:1200px;height:300px;background:linear-gradient(90deg,#e6ebf0,#f6f8fa 55%,#eef2f6)}
.greet-photo{left:0;top:2860px;width:540px;height:300px;background:linear-gradient(135deg,#dbe3ea,#b9c6d3 60%,#e3e9ef)}
.greet-text{left:620px;top:2950px;width:500px}
.greet-text h2{font-family:"Noto Serif JP",serif;font-size:28px;color:var(--navy);margin-bottom:16px;letter-spacing:.1em}
.greet-text p{font-size:13px;line-height:2}

/* footer */
.f-logo{left:60px;top:3200px;font-family:"Noto Serif JP",serif;font-size:26px;font-weight:700;color:var(--navy);letter-spacing:.1em}
.f-addr{left:60px;top:3246px;font-size:11px;color:var(--muted);line-height:1.6}
.f-tel{left:60px;top:3280px;font-size:30px;font-weight:700;color:var(--navy)}
.f-btn{left:330px;top:3204px;width:150px;height:42px}
.hours{left:60px;top:3330px;border-collapse:collapse;font-size:10px}
.hours th,.hours td{border:1px solid var(--line);padding:4px 8px;text-align:center}
.hours th{background:var(--pale);color:var(--navy);font-weight:500}
.hours td{color:var(--blue)}
.f-col{top:3204px;width:200px}
.f-col h4{font-size:13px;color:var(--navy);border-bottom:1px solid var(--line);padding-bottom:6px;margin-bottom:8px}
.f-col ul{list-style:none;display:grid;grid-template-columns:1fr 1fr;gap:6px 8px;font-size:10px;color:var(--muted)}
.map{left:0;top:3440px;width:1200px;height:540px;background:linear-gradient(135deg,#eef0ec,#e4e8e2 50%,#ecefe9)}
.map-card{left:20px;top:3460px;width:220px;height:90px;background:#fff;box-shadow:0 1px 4px rgba(0,0,0,.2);padding:10px;font-size:11px;line-height:1.6}
.pin{left:584px;top:3660px}
.copy{left:0;top:3980px;width:1200px;height:64px;background:var(--blue);color:#fff;text-align:center;font-size:11px;line-height:64px;letter-spacing:.06em}
</style>
</head>
<body>

<div class="abs hero" role="img" aria-label="白を基調とした明るい診療室の写真"></div>
<div class="abs topline">ショッピングモール内の小児・一般・矯正歯科 あおば歯科医院</div>
<div class="abs logo">あおば歯科医院</div>
<div class="abs contact">
  <div class="hours">診療時間 10:00〜19:00<br>休診日 モール休館日</div>
  <div class="tel">01-9876-5432</div>
  <div class="btn-web">WEBでご予約</div>
</div>
<nav class="abs nav">
  <div>トップページ<small>Top</small></div>
  <div>診療案内<small>Medical</small></div>
  <div>コンセプト<small>Concept</small></div>
  <div>お知らせ<small>News</small></div>
  <div>ご予約<small>Reserve</small></div>
</nav>
<div class="abs hero-copy">
  <h1>痛くない歯科治療</h1>
  <p>治療の痛みが怖い方や不安な方にも、<br>安心して通っていただけるよう、<br>あおば歯科医院では「痛くない歯科治療」<br>を心がけています。</p>
</div>
<div class="abs hero-btn">治療シミュレーション <span>&gt;</span></div>

<h2 class="abs sec-title" style="top:660px">歯のお悩みはありませんか</h2>
<p class="abs sec-lead" style="top:730px">笑顔の毎日のために、予防歯科からホワイトニングまで<br>幅広い診療科目をご用意しています。<br>お気軽にご相談ください。</p>

<div class="abs side-photo" role="img" aria-label="診療チェアのある診療室の写真"></div>
<div class="abs cards">
  <div class="card"><h3>小児歯科</h3><div class="icon" role="img" aria-label="子どもの歯のイラスト"></div><p>お子さまが楽しく通える<br>やさしい治療を行います</p></div>
  <div class="card"><h3>一般歯科</h3><div class="icon" role="img" aria-label="歯のイラスト"></div><p>むし歯や歯周病など<br>基本の治療を行います</p></div>
  <div class="card"><h3>矯正歯科</h3><div class="icon" role="img" aria-label="矯正装置のイラスト"></div><p>専門医による<br>矯正相談を行っています</p></div>
  <div class="card"><h3>ホワイトニング</h3><div class="icon" role="img" aria-label="白い歯のイラスト"></div><p>自然で明るい白い歯を<br>目指すお手伝いをします</p></div>
  <div class="card"><h3>インプラント治療</h3><div class="icon" role="img" aria-label="インプラントのイラスト"></div><p>失った歯を補う<br>治療をご提案します</p></div>
  <div class="card"><h3>予防歯科</h3><div class="icon" role="img" aria-label="歯ブラシのイラスト"></div><p>定期的なケアで<br>歯の健康を守ります</p></div>
  <div class="card"><h3>審美治療</h3><div class="icon" role="img" aria-label="輝く歯のイラスト"></div><p>見た目も美しい<br>歯を目指します</p></div>
  <div class="card"><h3>歯周病</h3><div class="icon" role="img" aria-label="歯ぐきのイラスト"></div><p>歯ぐきの状態を確認し<br>丁寧に治療します</p></div>
  <div class="card"><h3>レーザー治療</h3><div class="icon" role="img" aria-label="レーザー機器のイラスト"></div><p>痛みを抑えた<br>レーザー治療を行います</p></div>
</div>

<section class="abs concept" role="img" aria-label="青い色調の診療室の写真を背景にしたコンセプト">
  <h2 class="abs sec-title">あおば歯科医院のめざすもの</h2>
  <p class="abs en">患者様が安心して通える歯科医院を目指しています</p>
  <div class="abs circles">
    <div class="circle-item"><div class="circle"><span class="lbl">Concept</span><span class="num">01</span><b>痛くない<br>歯科治療</b></div><p>痛みに配慮した治療を<br>行っています</p></div>
    <div class="circle-item"><div class="circle"><span class="lbl">Concept</span><span class="num">02</span><b>お子様連れでも<br>安心の託児</b></div><p>キッズスペースで<br>お待ちいただけます</p></div>
    <div class="circle-item"><div class="circle"><span class="lbl">Concept</span><span class="num">03</span><b>何度も通院<br>させません</b></div><p>通院回数を抑えた<br>治療計画をご提案します</p></div>
  </div>
</section>

<h2 class="abs sec-title" style="top:2200px">あおば歯科医院からのお知らせ</h2>
<p class="abs sec-lead" style="top:2260px">医院からの最新情報をお届けします。</p>
<div class="abs news-photo" role="img" aria-label="観葉植物のある待合室の写真"></div>
<ul class="abs news-list">
  <li><span class="date">2019.10.10</span>お休みのお知らせ</li>
  <li><span class="date">2019.10.10</span>院内サービスを開始しました</li>
  <li><span class="date">2019.10.10</span>機器導入のお知らせ</li>
  <li><span class="date">2019.10.01</span>診療時間について</li>
  <li><span class="date">2019.09.30</span>連休中の診療について</li>
  <li><span class="date">2019.09.15</span>お休みのお知らせ</li>
  <li><span class="date">2019.09.01</span>定期検診のご案内</li>
  <li><span class="date">2019.08.20</span>院内設備のお知らせ</li>
  <li><span class="date">2019.08.10</span>夏季休診のお知らせ</li>
</ul>

<div class="abs greet"></div>
<div class="abs greet-photo" role="img" aria-label="白衣の院長の写真"></div>
<div class="abs greet-text">
  <h2>ごあいさつ</h2>
  <p>あおば歯科医院のホームページをご覧いただき、ありがとうございます。当院はショッピングモール内にあり、お買い物のついでにも気軽にお立ち寄りいただけます。患者様一人ひとりに寄り添い、安心して通える歯科医院を目指しております。</p>
</div>

<div class="abs f-logo">あおば歯科医院</div>
<div class="abs f-addr">〒000-0000 架空市みどり区1-2-3 モール2階</div>
<div class="abs f-tel">01-9876-5432</div>
<div class="abs btn-web f-btn" style="text-align:center;font-size:15px">WEBでご予約</div>
<table class="abs hours">
  <tr><th>診療時間</th><th>月</th><th>火</th><th>水</th><th>木</th><th>金</th><th>土</th><th>日</th></tr>
  <tr><th>10:00〜13:00</th><td>●</td><td>●</td><td>●</td><td>●</td><td>●</td><td>●</td><td>●</td></tr>
  <tr><th>14:30〜19:00</th><td>●</td><td>●</td><td>●</td><td>●</td><td>●</td><td>●</td><td>●</td></tr>
</table>
<div class="abs f-col" style="left:640px">
  <h4>診療科目</h4>
  <ul><li>小児歯科</li><li>一般歯科</li><li>矯正歯科</li><li>予防歯科</li><li>ホワイトニング</li><li>審美治療</li><li>インプラント</li><li>歯周病</li></ul>
</div>
<div class="abs f-col" style="left:900px">
  <h4>当院について</h4>
  <ul><li>トップページ</li><li>コンセプト</li><li>医院紹介</li><li>お知らせ</li><li>アクセス</li><li>ご予約</li></ul>
</div>

<div class="abs map" role="img" aria-label="医院周辺の地図"></div>
<div class="abs map-card"><b style="color:var(--navy)">あおば歯科医院</b><br>架空市みどり区1-2-3<br>モール2階</div>
<svg class="abs pin" width="32" height="44" viewBox="0 0 32 44"><path d="M16 0C7 0 0 7 0 16c0 12 16 28 16 28s16-16 16-28C32 7 25 0 16 0z" fill="#d94a3d"/><circle cx="16" cy="16" r="6" fill="#fff"/></svg>
<div class="abs copy">© AOBA DENTAL CLINIC. All Rights Reserved.</div>

</body>
</html>
```